Townhome Multi-Family Property Exterior Sign

Hello. We are looking for a new design for our exterior pylon for for a multi-family housing property in Texas. The design will need to go on a new sign panel to replace the existing (see photo of existing). We are looking to see both modern and contemporary designs. Included the sign should be the name, Loma Brisa Townhomes and the web address www.lomabrisatownhomes.example.

Attached here is a PDF file of the proposed new sign shape. We are open to other shape ideas as well if your design would better suit a more rectangular shape.

Industry/Entity Type

Property

Font styles to use
Serif
Sans Serif

Colors
9bcb3c

Requirements
Must have
• Name of building: Loma Brisa Townhomes
• Website: www.lomabrisatownhomes.example
Nice to have
• Address: 420-530 Halvorsen Lane (only if it fits nicely)

```html
<!DOCTYPE html>
<html lang="en">
<head>
<meta charset="utf-8">
<title>Loma Brisa Townhomes – Exterior Sign</title>
<link rel="stylesheet" href="https://fonts.googleapis.com/css2?family=Cinzel:wght@600&family=Raleway:wght@500&display=swap">
<style>
  :root {
    --backdrop: #9d9c9d;
    --backdrop-glow: #d9d8d9;
    --sign-green: #9bcb3c;
    --trim-white: #ffffff;
    --post-black: #231f20;
    --ink: #231f20;
  }
  html, body {
    margin: 0;
    padding: 0;
    overflow: hidden;
    background: var(--backdrop);
  }
  .sign-canvas {
    position: relative;
    width: 1200px;
    height: 644px;
    overflow: hidden;
    background: radial-gradient(ellipse 420px 260px at 600px 110px, var(--backdrop-glow), var(--backdrop) 100%);
  }
  .sign-art {
    position: absolute;
    inset: 0;
    display: block;
  }
  .post { fill: var(--post-black); }
  .panel { fill: var(--sign-green); }
  .trim-band { fill: none; stroke: var(--trim-white); stroke-width: 11; stroke-linejoin: miter; }
  .trim-line { fill: none; stroke: var(--trim-white); stroke-width: 2.5; }
  .crest { fill: var(--sign-green); }
  .crest-ornament { fill: url(#ornamentTone); }
  .property-name,
  .property-type {
    font-family: "Cinzel", serif;
    font-weight: 600;
    fill: var(--trim-white);
  }
  .property-name { font-size: 150px; }
  .property-type { font-size: 60px; }
  .web-address {
    font-family: "Raleway", sans-serif;
    font-weight: 500;
    font-size: 26px;
    fill: var(--ink);
  }
</style>
</head>
<body>
<main class="sign-canvas">
  <svg class="sign-art" viewBox="0 0 1200 644" width="1200" height="644" xmlns="http://www.w3.org/2000/svg">
    <defs>
      <radialGradient id="ornamentTone" cx="50%" cy="55%" r="60%">
        <stop offset="0%" stop-color="#f4f9e8"/>
        <stop offset="100%" stop-color="#c6e28c"/>
      </radialGradient>
    </defs>

    <!-- posts -->
    <g class="posts">
      <rect class="post" x="70" y="226" width="46" height="406"/>
      <polygon class="post" points="60,228 126,228 126,221 94,209 60,221"/>
      <rect class="post" x="1082" y="220" width="48" height="412"/>
      <polygon class="post" points="1072,222 1140,222 1140,214 1106,204 1072,214"/>
    </g>

    <!-- sign panel -->
    <path class="panel" d="M116,596 L116,234 C250,232 330,214 392,184 L808,184 C870,214 950,232 1082,234 L1082,596 Z"/>
    <path class="crest" d="M376,188 C376,160 410,142 450,140 C490,120 540,112 560,100 C572,70 585,48 600,48 C615,48 628,70 640,100 C660,112 710,120 750,140 C790,142 824,160 824,188 C824,200 810,206 800,206 L400,206 C390,206 376,200 376,188 Z"/>

    <!-- trim frame -->
    <path class="trim-band" d="M135,572 L135,262 C262,261 338,240 398,204 L802,204 C862,240 938,261 1066,262 L1066,572 Z"/>
    <path class="trim-line" d="M152,552 L152,280 C272,278 352,256 410,222 L790,222 C848,256 928,278 1048,280 L1048,552 Z"/>

    <!-- crest ornament area -->
    <path class="crest-ornament" role="img" aria-label="Decorative white scrollwork flourish crowning the sign"
          d="M392,180 C392,160 420,150 455,150 C495,132 545,122 565,110 C575,82 588,60 600,60 C612,60 625,82 635,110 C655,122 705,132 745,150 C780,150 808,160 808,180 C808,188 800,192 790,192 L410,192 C400,192 392,188 392,180 Z"/>

    <!-- property name -->
    <text class="property-name" x="600" y="405" text-anchor="middle" textLength="760" lengthAdjust="spacingAndGlyphs">Loma Brisa</text>
    <text class="property-type" x="600" y="488" text-anchor="middle" textLength="460" lengthAdjust="spacingAndGlyphs">TOWNHOMES</text>

    <!-- website -->
    <text class="web-address" x="600" y="538" text-anchor="middle" textLength="440" lengthAdjust="spacingAndGlyphs">www.lomabrisatownhomes.example</text>
  </svg>
</main>
</body>
</html>
```